Wrenfield Atelier, and interior design project management company!

We invite you to participate in our logo and web design contest for "Wrenfield Atelier Management Corp."!

Here's a brief description of our company paraphrased by ChatGPT.

Company Overview:
Wrenfield Atelier Management Corp. is your trusted partner for interior design project management, guided by international standards set forth by the Ordway Planning Council (OPC) and the Structured Delivery Reference Compendium (SDREF). With a commitment to excellence, we seamlessly merge modern project management techniques with traditional values, emphasizing quality and attention to detail in every project.

Our Unique Strengths:

Local Fabrication Facility: What sets us apart is our in-house fabrication facility, a millwork shop with an impressive 20 years of experience. This facility empowers us to exercise meticulous control over the production process, ensuring that your project is crafted with precision and care right in our local community.

Experienced Skilled Workers: At Wrenfield Atelier Management Corp., our team comprises highly skilled and experienced craftsmen and artisans. They bring years of expertise to every project, guaranteeing that your interior design visions are brought to life with unmatched skill and finesse.

Serving Commercial and Residential Clients:
Our primary focus is on serving commercial clients, specializing in Tenant Improvement (TI) projects. We understand the unique demands of commercial spaces, and our project management expertise ensures that your commercial interior design projects are executed efficiently and within budget.

In addition to our commercial expertise, we also cater to discerning residential clients who seek that extra level of attention to detail. Our comprehensive services encompass all types of projects, from commercial tenant improvements to residential renovations. Regardless of the project's scale or scope, you can trust that all aspects will be managed seamlessly by our professional team.

Why Choose Us:
We are not just project managers; we are passionate advocates for your project's success. By adhering to OPC and SDREF standards, we deliver project management that is structured, efficient, and dependable. Our commitment to personal and approachable service, combined with our dedication to quality craftsmanship, ensures that your interior design projects are executed flawlessly from start to finish.

With Wrenfield Atelier Management Corp., you can trust that your project will benefit from the perfect blend of modern project management techniques and traditional values, resulting in interiors that are not only aesthetically pleasing but also built to stand the test of time.

Whether you require a commercial TI project or a residential project with meticulous attention to detail, we are the one-stop professional company that can bring your vision to life. Join our logo design contest, and let's together represent our dedication to excellence in project management and craftsmanship for both commercial and residential clients.

Target Market(s)

interior designers and architects, business owners

Industry/Entity Type

construction, project management, interior design, custom millwork and cabinets

Number of Pages Required

1 page

Requirements
Must have
• General consideration for design to float from social media to website.
Nice to have
• Consideration for more sophisticated backend support for customer support and project management update integrations apps such as ClickUp. (Technical portion not part of scope of work.)

```html
<!DOCTYPE html>
<html lang="en">
<head>
<meta charset="utf-8">
<title>Wrenfield Atelier Management Corp.</title>
<link rel="stylesheet" href="https://fonts.googleapis.com/css2?family=DM+Sans:wght@400;500;700&display=swap">
<style>
:root{
  --stage:#d4d5d7;
  --teal:#4fc1c9;
  --ink:#2b2b2d;
  --dark:#363537;
  --card:#454446;
  --card-line:#8a8a8c;
  --light:#e6e7e9;
  --mid:#d3d4d6;
  --white:#ffffff;
  --field:#e3e4e6;
  --social:#2357c4;
}
*{box-sizing:border-box;margin:0;padding:0}
html,body{width:1200px;height:1200px;overflow:hidden;background:var(--stage)}
body{font-family:"DM Sans",Arial,sans-serif;color:var(--ink)}
.frame{position:absolute;left:473px;top:12px;width:252px;height:1175px;overflow:hidden;box-shadow:0 0 6px rgba(0,0,0,.08)}
.page{position:absolute;left:0;top:0;width:1280px;height:5976px;transform:scale(.19662);transform-origin:0 0;background:var(--white)}
section,footer{position:absolute;left:0;width:1280px}
.abs{position:absolute}
.photo{position:absolute}

/* hero */
.hero{top:0;height:746px;background:var(--white)}
.brand{position:absolute;left:48px;top:40px;font-weight:700;font-size:19px;line-height:20px;letter-spacing:.3px;text-transform:uppercase;color:var(--ink)}
.hero-photo{left:0;top:0;width:1280px;height:746px;background:linear-gradient(135deg,#d9cdbd 0%,#efe8de 40%,#c9b49a 75%,#9a7a62 100%);clip-path:polygon(641px 0,1280px 0,1280px 746px,493px 746px)}
.nav{position:absolute;top:38px;right:40px;display:flex;gap:30px;align-items:center}
.hero-title{left:145px;top:192px;width:380px;font-size:29px;line-height:38px;font-weight:400;color:var(--teal)}
.hero-title b{font-weight:500}
.hero-text{left:145px;top:402px;width:370px;font-size:13.5px;line-height:22px}
.btn{display:inline-block;border:2px solid var(--ink);border-radius:20px;font-weight:500;font-size:14px;padding:7px 16px;color:var(--ink);background:var(--white)}
.hero .btn{position:absolute;left:145px;top:584px}

/* strengths */
.strengths{top:746px;height:1027px;background:var(--dark)}
h2{font-weight:500;color:var(--teal);text-align:center}
.strengths h2{position:absolute;top:106px;width:100%;font-size:50px}
.cards{position:absolute;left:130px;top:278px;width:1023px;height:597px;display:flex;border:2px solid var(--card-line)}
.card{flex:1;background:var(--card);border-right:2px solid var(--card-line);text-align:center;padding:30px 34px 0;position:relative}
.card:last-child{border-right:0}
.card.is-active{outline:4px solid var(--white);outline-offset:-2px;z-index:1}
.card svg{display:block;margin:0 auto 60px}
.card h3{font-size:19px;line-height:28px;font-weight:500;color:var(--teal);margin-bottom:18px}
.card p{font-size:14.5px;line-height:21px;color:#e4e4e4}
.card .more{position:absolute;left:0;right:0;bottom:34px;font-size:14px;color:#bdbdbd}

/* why */
.why{top:1773px;height:1381px;background:var(--white)}
.why h2{position:absolute;top:96px;width:100%;font-size:50px}
.row{position:absolute;left:123px;width:1021px}
.row1{top:243px;height:335px;background:var(--light)}
.row2{top:578px;height:332px;background:var(--mid)}
.row3{top:910px;height:363px;background:var(--light)}
.row .photo{width:395px;height:230px;border-radius:12px}
.row p{position:absolute;width:345px;font-size:13.5px;line-height:21.5px}

/* wide photo */
.wide{top:3154px;height:676px;background:linear-gradient(120deg,#3c4452 0%,#7f8a99 35%,#c5ccd6 60%,#5c6d8f 85%,#2c3a5e 100%)}

/* leading */
.leading{top:3830px;height:560px;background:var(--white)}
.leading h2{position:absolute;top:100px;width:100%;font-size:42px;line-height:52px}
.ticks{position:absolute;top:302px;list-style:none}
.ticks li{display:flex;align-items:center;gap:14px;height:50px;font-size:19px}

/* cta */
.cta{top:4390px;height:477px;background:var(--dark)}
.cta-photo{left:0;top:0;width:1280px;height:477px;background:linear-gradient(110deg,#6d5a48 0%,#a78f6e 30%,#6f9e80 55%,#a5713f 80%,#5b4431 100%);clip-path:polygon(0 0,578px 0,493px 477px,0 477px)}
.cta h3{position:absolute;left:638px;top:72px;font-size:44px;line-height:57px;font-weight:500;color:var(--teal)}
.cta p{position:absolute;left:638px;top:202px;width:540px;font-size:19px;line-height:29px;color:#eeeeee}
.cta .btn{position:absolute;left:638px;top:354px;border-color:var(--white);color:var(--ink)}

/* contact */
.contact{top:4867px;height:717px;background:var(--white)}
.contact h2{position:absolute;top:70px;width:100%;font-size:42px;line-height:52px;font-weight:400}
.field{position:absolute;height:41px;background:var(--field);border:1px solid #c9cacc;border-radius:3px;font-size:14px;padding:11px 14px;color:#444}
.field.tall{height:180px}
.badge{position:absolute;left:1060px;top:552px;width:80px;height:78px;background:#f4f4f4;border:1px solid #d6d6d6;border-radius:3px}
.contact .btn{position:absolute;left:559px;top:604px;width:162px;text-align:center}

/* footer */
.site-footer{top:5584px;height:392px;background:var(--light);border-top:6px solid var(--teal)}
.site-footer .brand{left:145px;top:66px}
.foot-info{position:absolute;left:145px;top:150px;font-size:12px;line-height:16px}
.social{position:absolute;left:938px;top:138px;display:flex;gap:12px}
.social span{width:38px;height:38px;border-radius:50%;background:var(--social)}
.rule{position:absolute;left:145px;right:140px;top:272px;height:1px;background:#c6c7c9}
.legal{position:absolute;top:292px;width:100%;text-align:center;font-size:12.5px;line-height:19px}
</style>
</head>
<body>
<div class="frame">
<div class="page">

  <section class="hero">
    <div class="photo hero-photo" role="img" aria-label="Bright living room with floating staircase, beige sofa and round patterned rug"></div>
    <div class="brand">Wrenfield Atelier<br>Management<br>Corp.</div>
    <nav class="nav" aria-label="Header tools">
      <svg width="20" height="20" viewBox="0 0 20 20"><circle cx="8" cy="8" r="6" fill="none" stroke="#222" stroke-width="2"/><line x1="12.5" y1="12.5" x2="18" y2="18" stroke="#222" stroke-width="2"/></svg>
      <svg width="60" height="20" viewBox="0 0 60 20"><circle cx="6" cy="10" r="4" fill="none" stroke="#222" stroke-width="2"/><rect x="16" y="3" width="30" height="14" rx="7" fill="none" stroke="#222" stroke-width="2"/><circle cx="38" cy="10" r="4" fill="#222"/><path d="M52 5a5 5 0 1 0 5 8 4 4 0 0 1-5-8z" fill="#222"/></svg>
      <svg width="26" height="18" viewBox="0 0 26 18"><rect y="1" width="26" height="2" fill="#222"/><rect y="8" width="26" height="2" fill="#222"/><rect x="8" y="15" width="18" height="2" fill="#222"/></svg>
    </nav>
    <h1 class="abs hero-title"><b>Wrenfield Atelier Management Corp.</b> is your trusted partner for interior design project management</h1>
    <p class="abs hero-text">Guided by international standards set forth by the Ordway Planning Council (OPC) and the Structured Delivery Reference Compendium. With a commitment to excellence, we seamlessly merge modern project management techniques with traditional values, emphasizing quality and attention to detail in every project.</p>
    <a class="btn">Contact Us Today</a>
  </section>

  <section class="strengths">
    <h2>Our Unique Strengths</h2>
    <div class="cards">
      <article class="card">
        <svg width="40" height="64" viewBox="0 0 40 64"><path d="M22 2c6 14-14 22-8 40 3 10 14 14 14 14S12 48 16 32c3-12 12-16 6-30z" fill="none" stroke="var(--teal)" stroke-width="4"/></svg>
        <h3>Local Fabrication Facility</h3>
        <p>What sets us apart is our in-house fabrication facility, a millwork shop with an impressive 20 years of experience. This facility empowers us to exercise meticulous control over the production process, ensuring that your project is crafted with precision and care right in our local community.</p>
        <span class="more">Learn more ↗</span>
      </article>
      <article class="card is-active">
        <svg width="50" height="64" viewBox="0 0 50 64" fill="var(--teal)"><circle cx="25" cy="8" r="3"/><circle cx="19" cy="20" r="3"/><circle cx="31" cy="20" r="3"/><circle cx="13" cy="32" r="3.5"/><circle cx="25" cy="32" r="3.5"/><circle cx="37" cy="32" r="3.5"/><circle cx="8" cy="46" r="4"/><circle cx="19" cy="46" r="4"/><circle cx="31" cy="46" r="4"/><circle cx="42" cy="46" r="4"/><circle cx="13" cy="58" r="4.5"/><circle cx="25" cy="58" r="4.5"/><circle cx="37" cy="58" r="4.5"/></svg>
        <h3>Experienced Skilled Workers</h3>
        <p>At Wrenfield Atelier Management Corp., our team comprises highly skilled and experienced craftsmen and artisans. They bring years of expertise to every project, guaranteeing that your interior design visions are brought to life with unmatched skill and finesse.</p>
        <span class="more">Learn more ↗</span>
      </article>
      <article class="card">
        <svg width="64" height="64" viewBox="0 0 64 64" fill="none" stroke="var(--teal)" stroke-width="2.5"><path d="M32 58V14M32 58L14 24M32 58L50 24M32 58L4 40M32 58L60 40M32 58L22 18M32 58L42 18M4 58h56"/></svg>
        <h3>Serving Commercial and Residential Clients</h3>
        <p>Our primary focus is on serving commercial clients, specializing in Tenant Improvement (TI) projects. We understand the unique demands of commercial spaces, and our project management expertise ensures that your projects within budget.</p>
        <span class="more">Learn more ↗</span>
      </article>
      <article class="card">
        <svg width="56" height="64" viewBox="0 0 56 64" fill="var(--teal)"><path d="M28 6l24 13-24 13L4 19z"/><path d="M4 30l24 13 24-13v7L28 50 4 37z"/><path d="M4 44l24 13 24-13v5L28 62 4 49z" opacity=".8"/></svg>
        <h3>extra level of attention to detail</h3>
        <p>Our comprehensive services encompass all types of projects, from commercial tenant improvements to residential renovations. Regardless of the project's scale or scope, you can trust that all aspects will be managed seamlessly by our professional team.</p>
        <span class="more">Learn more ↗</span>
      </article>
    </div>
  </section>

  <section class="why">
    <h2>Why Choose Us</h2>
    <div class="row row1">
      <div class="photo" style="left:44px;top:51px;background:linear-gradient(120deg,#e8ecef,#b9c6d3 50%,#6b7f95)" role="img" aria-label="White living room with a tree mural and a white sofa"></div>
      <p style="left:484px;top:70px">We are not just project managers; we are passionate advocates for your project's success. By adhering to OPC and SDREF standards, we deliver project management that is structured, efficient, and dependable. Our commitment to personal and approachable service, combined with our dedication to quality craftsmanship, ensures that your interior design projects are executed flawlessly from start to finish.</p>
    </div>
    <div class="row row2">
      <p style="left:225px;top:90px"><b>With Wrenfield Atelier Management Corp.</b>, you can trust that your project will benefit from the perfect blend of modern project management techniques and traditional values, resulting in interiors that are not only aesthetically pleasing but also built to stand the test of time.</p>
      <div class="photo" style="left:583px;top:48px;background:linear-gradient(120deg,#f2f2f0,#d9b48c 45%,#3b5fa8 60%,#efefed)" role="img" aria-label="Bright room with wooden and blue cube shelving and a white chair"></div>
    </div>
    <div class="row row3">
      <div class="photo" style="left:44px;top:51px;background:linear-gradient(120deg,#3a3835,#7a7570 40%,#b3363a 65%,#5d5a55)" role="img" aria-label="Long lounge corridor with rows of red armchairs"></div>
      <p style="left:484px;top:80px">Whether you require a commercial TI project or a residential project with meticulous attention to detail, we are the one-stop professional company that can bring your vision to life. Join our logo design contest, and let's together represent our dedication to excellence in project management and craftsmanship for both commercial and residential clients.</p>
    </div>
  </section>

  <section class="wide photo" role="img" aria-label="Living room with navy sectional sofa, wall television and a sea and mountain view"></section>

  <section class="leading">
    <h2>Leading in construction,<br>project management, interior design,<br>custom millwork and cabinets.</h2>
    <ul class="ticks" style="left:174px">
      <li><svg width="22" height="22" viewBox="0 0 22 22"><circle cx="11" cy="11" r="11" fill="var(--teal)"/><path d="M6 11l3.5 3.5L16 8" fill="none" stroke="#fff" stroke-width="2.4"/></svg>Lorem ipsum dolor sit amet</li>
      <li><svg width="22" height="22" viewBox="0 0 22 22"><circle cx="11" cy="11" r="11" fill="var(--teal)"/><path d="M6 11l3.5 3.5L16 8" fill="none" stroke="#fff" stroke-width="2.4"/></svg>Consectetur adipiscing elit</li>
      <li><svg width="22" height="22" viewBox="0 0 22 22"><circle cx="11" cy="11" r="11" fill="var(--teal)"/><path d="M6 11l3.5 3.5L16 8" fill="none" stroke="#fff" stroke-width="2.4"/></svg>Sed do eiusmod tempor incididunt</li>
    </ul>
    <ul class="ticks" style="left:711px">
      <li><svg width="22" height="22" viewBox="0 0 22 22"><circle cx="11" cy="11" r="11" fill="var(--teal)"/><path d="M6 11l3.5 3.5L16 8" fill="none" stroke="#fff" stroke-width="2.4"/></svg>Ut enim ad minim veniam</li>
      <li><svg width="22" height="22" viewBox="0 0 22 22"><circle cx="11" cy="11" r="11" fill="var(--teal)"/><path d="M6 11l3.5 3.5L16 8" fill="none" stroke="#fff" stroke-width="2.4"/></svg>Quis nostrud exercitation ullamco</li>
      <li><svg width="22" height="22" viewBox="0 0 22 22"><circle cx="11" cy="11" r="11" fill="var(--teal)"/><path d="M6 11l3.5 3.5L16 8" fill="none" stroke="#fff" stroke-width="2.4"/></svg>Duis aute irure dolor in reprehenderit</li>
    </ul>
  </section>

  <section class="cta">
    <div class="photo cta-photo" role="img" aria-label="Library lounge with green tiled fireplace, tall bookshelves and a rug"></div>
    <h3>Ready<br>to Discover?</h3>
    <p>Lorem ipsum dolor sit amet, consectetur adipiscing elit, sed do eiusmod tempor incididunt ut labore et dolore magna aliqua. Ut enim ad minim veniam, quis nostrud exercitation ullamco laboris.</p>
    <a class="btn">Request a Quote</a>
  </section>

  <section class="contact">
    <h2>Have a need<br>or an idea you'd like<br>to run by us?</h2>
    <div class="field" style="left:142px;top:287px;width:484px">Name</div>
    <div class="field" style="left:142px;top:356px;width:484px">Address</div>
    <div class="field" style="left:142px;top:423px;width:484px">Phone</div>
    <div class="field" style="left:142px;top:490px;width:484px">Email</div>
    <div class="field" style="left:654px;top:287px;width:487px">Subject<svg style="position:absolute;right:14px;top:15px" width="14" height="9" viewBox="0 0 14 9"><path d="M1 1l6 6 6-6" fill="none" stroke="#555" stroke-width="1.8"/></svg></div>
    <div class="field tall" style="left:654px;top:354px;width:487px">Message</div>
    <div class="badge" aria-hidden="true"></div>
    <a class="btn">Submit</a>
  </section>

  <footer class="site-footer">
    <div class="brand">Wrenfield Atelier<br>Management<br>Corp.</div>
    <div class="foot-info"><b>Contact our experts:</b><br>48 Alder Row, Brookhaven, ST 20418<br>P 0200 555 014 - 0200 555 015<br>E hello@wrenfield-atelier.example</div>
    <div class="social" aria-label="Social links"><span></span><span></span><span></span><span></span></div>
    <div class="rule"></div>
    <p class="legal">Copyright © 2023, Wrenfield Atelier Management Corp.<br>Privacy Policy | Term of Services</p>
  </footer>

</div>
</div>
</body>
</html>
```